Attorney Business Card

I need a business card that looks professional yet modern. I am an Attorney. , I need a professional yet modern business card for my law practice. My logo and information have been uploaded. , I need a business card that looks professional yet modern. I am an Attorney. , I need a professional yet modern business card for my law practice. My logo and information have been uploaded.

Industry/Entity Type

Business

Requirements
Must have
• My logo which has been uploaded , my logo , My logo which has been uploaded , my logo

```html
<!DOCTYPE html>
<html lang="en">
<head>
<meta charset="utf-8">
<title>Marrowfield Law Firm – Business Card</title>
<link href="https://fonts.googleapis.com/css2?family=Raleway:wght@400;500;600&family=Open+Sans:wght@400;600&display=swap" rel="stylesheet">
<style>
  :root {
    --backdrop: #161617;
    --card-dark: #262629;
    --card-light: #3b3b3f;
    --accent: #2aa9e0;
    --text-light: #f1f1f1;
    --text-muted: #d6d6d6;
  }
  * { margin: 0; padding: 0; box-sizing: border-box; }
  html, body { width: 932px; height: 1200px; overflow: hidden; }
  body { background: var(--backdrop); position: relative; font-family: "Open Sans", sans-serif; }

  .card {
    position: absolute;
    left: 86px;
    width: 760px;
    height: 434px;
    background: linear-gradient(135deg, var(--card-light) 0%, var(--card-dark) 55%, #1f1f22 100%);
    border-radius: 4px;
    overflow: hidden;
    box-shadow: 0 10px 30px rgba(0,0,0,0.5);
  }
  .card--front { top: 140px; }
  .card--back { top: 660px; }

  /* front */
  .front-mark {
    position: absolute; left: 0; right: 0; top: 110px;
    display: flex; flex-direction: column; align-items: center; gap: 26px;
  }
  .mark-dot {
    width: 96px; height: 96px; border-radius: 50%;
    border: 3px solid var(--accent);
  }
  .firm-name {
    font-family: "Raleway", sans-serif; font-weight: 600;
    color: var(--accent); font-size: 42px; letter-spacing: 4px;
    text-transform: uppercase; white-space: nowrap;
  }

  /* back */
  .back-mark {
    position: absolute; left: 34px; top: 34px; width: 220px;
    display: flex; flex-direction: column; align-items: center; gap: 12px;
  }
  .back-mark .mark-dot { width: 70px; height: 70px; border-width: 2px; }
  .back-mark .firm-name { font-size: 14px; letter-spacing: 1.5px; }

  .identity { position: absolute; left: 300px; top: 48px; font-family: "Raleway", sans-serif; text-transform: uppercase; }
  .identity__name { color: var(--accent); font-size: 27px; font-weight: 400; letter-spacing: 1px; }
  .identity__title { color: var(--text-light); font-size: 22px; font-weight: 400; letter-spacing: 1px; margin-top: 4px; }

  .divider { position: absolute; left: 40px; right: 0; top: 172px; height: 2px; background: var(--accent); }

  .address {
    position: absolute; left: 52px; top: 206px;
    color: var(--text-light); font-size: 17px; line-height: 1.5; text-transform: uppercase;
  }
  .phones { position: absolute; left: 450px; top: 200px; list-style: none; }
  .phones li {
    display: flex; align-items: center; gap: 12px;
    color: var(--text-light); font-size: 17px; line-height: 1; margin-bottom: 9px; text-transform: uppercase;
  }
  .phones svg, .contact-band svg { width: 18px; height: 18px; fill: var(--text-light); flex: none; }

  .contact-band {
    position: absolute; left: 0; right: 0; bottom: 0; height: 62px;
    background: var(--accent);
    display: flex; align-items: center; padding: 0 52px;
    color: #fff; font-size: 16px; text-transform: uppercase; font-weight: 600;
  }
  .contact-band span { display: flex; align-items: center; gap: 12px; }
  .contact-band .web { margin-left: auto; margin-right: 90px; }
</style>
</head>
<body>

  <section class="card card--front" aria-label="Card front">
    <div class="front-mark">
      <div class="mark-dot"></div>
      <div class="firm-name">Marrowfield Law Firm</div>
    </div>
  </section>

  <section class="card card--back" aria-label="Card back">
    <div class="back-mark">
      <div class="mark-dot"></div>
      <div class="firm-name">Marrowfield Law Firm</div>
    </div>

    <div class="identity">
      <div class="identity__name">Daniel Marrowfield, Esq.</div>
      <div class="identity__title">Attorney at Law</div>
    </div>

    <div class="divider"></div>

    <address class="address" style="font-style:normal">
      2270 Cedarline Ave.<br>
      Penthouse<br>
      Westbrook, CA 90418
    </address>

    <ul class="phones">
      <li>
        <svg viewBox="0 0 24 24" aria-hidden="true"><path d="M6.6 10.8a15 15 0 0 0 6.6 6.6l2.2-2.2a1 1 0 0 1 1-.25 11.4 11.4 0 0 0 3.6.57 1 1 0 0 1 1 1V20a1 1 0 0 1-1 1A17 17 0 0 1 3 4a1 1 0 0 1 1-1h3.5a1 1 0 0 1 1 1c0 1.25.2 2.45.57 3.57a1 1 0 0 1-.25 1z"/></svg>
        310.555.0142 Tel
      </li>
      <li>
        <svg viewBox="0 0 24 24" aria-hidden="true"><path d="M6 2h10l2 2v5H6zM3 10h18v9h-3v3H6v-3H3zm5 6v4h8v-4z"/></svg>
        310.555.0198 Fax
      </li>
      <li>
        <svg viewBox="0 0 24 24" aria-hidden="true"><path d="M7 1h10a2 2 0 0 1 2 2v18a2 2 0 0 1-2 2H7a2 2 0 0 1-2-2V3a2 2 0 0 1 2-2zm0 3v14h10V4zm5 15.5a1 1 0 1 0 0 2 1 1 0 0 0 0-2z"/></svg>
        310.555.0176 Mobile
      </li>
    </ul>

    <div class="contact-band">
      <span class="email">
        <svg viewBox="0 0 24 24" aria-hidden="true"><path d="M2 5h20v14H2zm2 2v.5l8 5 8-5V7zm0 3v7h16v-7l-8 5z"/></svg>
        daniel@mwlawfirm.com
      </span>
      <span class="web">
        <svg viewBox="0 0 24 24" aria-hidden="true"><path d="M12 2a10 10 0 1 0 0 20 10 10 0 0 0 0-20zm6.9 6h-3a15 15 0 0 0-1.3-3.9A8 8 0 0 1 18.9 8zM12 4c.8 1.1 1.5 2.5 1.9 4h-3.8c.4-1.5 1.1-2.9 1.9-4zM4.3 14a8 8 0 0 1 0-4h3.4a16 16 0 0 0 0 4zm.8 2h3a15 15 0 0 0 1.3 3.9A8 8 0 0 1 5.1 16zm3-8h-3a8 8 0 0 1 4.3-3.9A15 15 0 0 0 8.1 8zM12 20c-.8-1.1-1.5-2.5-1.9-4h3.8c-.4 1.5-1.1 2.9-1.9 4zm2.3-6H9.7a14 14 0 0 1 0-4h4.6a14 14 0 0 1 0 4zm.3 5.9a15 15 0 0 0 1.3-3.9h3a8 8 0 0 1-4.3 3.9zm1.7-5.9a16 16 0 0 0 0-4h3.4a8 8 0 0 1 0 4z"/></svg>
        www.mwlawfirm.com
      </span>
    </div>
  </section>

</body>
</html>
```